RM Tomás Rivera (Business Card)

Hi designers, in this work, I'm looking for an sophisticated stylish, elegant and proffesional personal card. We have a laboratory of pathology automated, with equipments high quality.
In this web the designers, have created my business logo, the name is "RM Tomás Rivera"
In our lab, we principal work is to prepare the biopsies for further diagnostic of diseases like cancer, tumors, etc.
I need that the first face, only having my complete logo (Rm Tomás Rivera, Laboratorio de procesamiento Histologico)
The overleaf, could repeat the same logo, like water logo.
In this face, I need to say: My full data:

Técnico en Anatomía Patológica
Tomás Rivera Ibarra M.P 47203
Av. Paredes Luján 418 - 2do piso - Instituto Marbel.
Córdoba, Argentina
(0351) 154820937
rivera.tomas@correolab.example

with respect the colors of card, use your imagination, the original logo color is violet, I haven't chosen a color base for the card.

attached pictures are examples of cards I like your DESIGN.
Attached too, the original logo to my company.

the size of card are:
horizontal: 9cm
vertical: 5,5cm

any question that you have, not doubt to question me,
Hand to work!

Industry/Entity Type

Laboratory

Requirements
Must have
• designers sophisticated, not simples, like show the images attached

```html
<!DOCTYPE html>
<html lang="es">
<head>
<meta charset="utf-8">
<title>RM Tomás Rivera – Tarjetas personales</title>
<link href="https://fonts.googleapis.com/css2?family=Open+Sans:ital,wght@0,400;0,600;1,400&family=Roboto+Condensed:wght@500&display=swap" rel="stylesheet">
<style>
  :root {
    --violet: #652d8f;
    --violet-mid: #8566b6;
    --violet-deep: #5a3893;
    --violet-soft: #b4a3d4;
    --violet-pale: #cfc3e4;
    --grey: #5f5f62;
    --grey-text: #58585b;
    --frame-grey: #6d6e71;
    --ink: #111;
    --paper: #ffffff;
  }
  * { margin: 0; padding: 0; box-sizing: border-box; }
  html, body {
    width: 1200px; height: 808px; overflow: hidden;
    background: var(--paper);
  }
  .sheet { position: relative; width: 1200px; height: 808px; }

  .card {
    position: absolute;
    width: 553px; height: 337px;
    border: 2px solid var(--ink);
    border-radius: 27px;
    overflow: hidden;
    background: var(--paper);
    font-family: "Open Sans", Arial, sans-serif;
  }
  .card--front-plain { left: 40px; top: 40px; }
  .card--back-violet { left: 613px; top: 44px; height: 341px; background: var(--violet); color: #fff; }
  .card--front-framed { left: 43px; top: 427px; height: 336px; }
  .card--back-wave { left: 616px; top: 427px; height: 336px; color: var(--grey-text); }

  /* Brand lockup */
  .brand {
    position: absolute; left: 0; right: 0;
    display: flex; flex-direction: column; align-items: center;
  }
  .brand__mark {
    width: 46px; height: 46px;
    border: 3px solid var(--violet);
    margin-bottom: 12px;
  }
  .brand__name {
    font-family: "Open Sans", Arial, sans-serif;
    font-weight: 400;
    font-size: 16px;
    letter-spacing: 7px;
    color: var(--grey);
    text-transform: uppercase;
    padding-bottom: 3px;
    border-bottom: 1.5px solid var(--grey);
    width: 310px;
    text-align: center;
  }
  .brand__tagline {
    font-family: "Roboto Condensed", "Arial Narrow", sans-serif;
    font-weight: 500;
    font-size: 19.5px;
    color: var(--grey);
    margin-top: 4px;
    letter-spacing: -0.2px;
  }
  .card--front-plain .brand { top: 97px; }
  .card--front-framed .brand { top: 55px; }

  /* Contact details */
  .details {
    position: absolute; left: 0; right: 0;
    text-align: center;
  }
  .details__role { font-size: 15.5px; }
  .details__name { font-style: italic; font-size: 21.5px; margin-top: 22px; }
  .details__address { font-size: 14.5px; line-height: 21px; margin-top: 14px; }
  .details__phone { font-size: 18px; line-height: 28px; margin-top: 20px; }
  .card--back-violet .details { top: 59px; }
  .card--back-wave .details { top: 24px; }

  .frame, .waves { position: absolute; left: 0; top: 0; }
  .waves { top: auto; bottom: 0; }
</style>
</head>
<body>
<main class="sheet">

  <!-- Front, plain -->
  <section class="card card--front-plain" aria-label="Frente de tarjeta">
    <div class="brand">
      <span class="brand__mark" aria-hidden="true"></span>
      <span class="brand__name">RM Tomás Rivera</span>
      <span class="brand__tagline">LABORATORIO DE PROCESAMIENTO HISTOLOGICO</span>
    </div>
  </section>

  <!-- Back, violet -->
  <section class="card card--back-violet" aria-label="Dorso de tarjeta violeta">
    <div class="details">
      <p class="details__role">Técnico en Anatomía Patológica</p>
      <p class="details__name">Tomás Rivera Ibarra M.P 47203</p>
      <p class="details__address">Av. Paredes Luján 418 - 2do piso - Instituto Marbel.<br>Córdoba, Argentina</p>
      <p class="details__phone">(0351) 154820937<br>rivera.tomas@correolab.example</p>
    </div>
  </section>

  <!-- Front, framed with waves -->
  <section class="card card--front-framed" aria-label="Frente de tarjeta con marco">
    <svg class="frame" width="553" height="336" viewBox="0 0 553 336" aria-hidden="true">
      <polyline points="155,10 117,10 30,122 117,234 155,234" fill="none" stroke="var(--frame-grey)" stroke-width="6" stroke-linejoin="miter"/>
      <polyline points="398,10 436,10 523,122 436,234 398,234" fill="none" stroke="var(--violet)" stroke-width="6" stroke-linejoin="miter"/>
    </svg>
    <div class="brand">
      <span class="brand__mark" aria-hidden="true"></span>
      <span class="brand__name">RM Tomás Rivera</span>
      <span class="brand__tagline">LABORATORIO DE PROCESAMIENTO HISTOLOGICO</span>
    </div>
    <svg class="waves" width="553" height="90" viewBox="0 0 553 90" preserveAspectRatio="none" aria-hidden="true">
      <path d="M0,14 C140,-4 300,6 553,20 L553,90 L0,90 Z" fill="var(--violet-pale)"/>
      <path d="M0,26 C150,12 320,22 553,34 L553,90 L0,90 Z" fill="var(--violet-mid)"/>
      <path d="M0,40 C160,24 330,38 553,42 L553,90 L0,90 Z" fill="var(--violet-deep)"/>
      <path d="M0,46 C170,30 340,44 553,50 L553,90 L0,90 Z" fill="var(--violet-soft)"/>
    </svg>
  </section>

  <!-- Back, white with waves -->
  <section class="card card--back-wave" aria-label="Dorso de tarjeta blanco">
    <div class="details">
      <p class="details__role">Técnico en Anatomía Patológica</p>
      <p class="details__name">Tomás Rivera Ibarra M.P 47203</p>
      <p class="details__address">Av. Paredes Luján 418 - 2do piso - Instituto Marbel.<br>Córdoba, Argentina</p>
      <p class="details__phone">(0351) 154820937<br>rivera.tomas@correolab.example</p>
    </div>
    <svg class="waves" width="553" height="90" viewBox="0 0 553 90" preserveAspectRatio="none" aria-hidden="true">
      <path d="M0,14 C140,-4 300,6 553,20 L553,90 L0,90 Z" fill="var(--violet-pale)"/>
      <path d="M0,26 C150,12 320,22 553,34 L553,90 L0,90 Z" fill="var(--violet-mid)"/>
      <path d="M0,40 C160,24 330,38 553,42 L553,90 L0,90 Z" fill="var(--violet-deep)"/>
      <path d="M0,46 C170,30 340,44 553,50 L553,90 L0,90 Z" fill="var(--violet-soft)"/>
    </svg>
  </section>

</main>
</body>
</html>
```